Landcape Construction Company needs a flyer to catch attention

A flyer that can be displayed at several different stores detailing our skills, work produced, experience and contact details. Information can be extracted from our website www.brvkw.co.nz. The flyer should feel very green, with addition of pics of work completed as well as stock images of lush green plants, lawns, landscape or similar. Needs to be eye catching with just enough information to express our experience and commitment to high standards

Target Market(s)

Residential
Landscape Architects

Industry/Entity Type

Landscaping

Font styles to use
Serif

Colors
abd037

Requirements
Must have
• Our logo
Experience
Services offered including pictures
All information avail on our website www.brvkw.co.nz
Nice to have
• stock images of lush greenery like a garden after fresh rainfall
Should not have
• Nothing comes to mind

```html
<!DOCTYPE html>
<html lang="en">
<head>
<meta charset="utf-8">
<title>Greenvale Landscaping Co – Flyer</title>
<link href="https://fonts.googleapis.com/css2?family=Montserrat:wght@300;400;700;800&family=Montserrat+Alternates:wght@700&display=swap" rel="stylesheet">
<style>
  :root{
    --lime:#abd037;
    --green:#3aaa35;
    --forest:#0f8a3c;
    --ink:#2b2b2b;
    --band:#2e2e2e;
    --paper:#ffffff;
    --backdrop:#e9e9e9;
    --muted:#4a4a4a;
  }
  *{box-sizing:border-box;margin:0;padding:0}
  html,body{width:1200px;height:2218px;overflow:hidden;background:var(--backdrop)}
  body{font-family:"Montserrat",Arial,sans-serif;position:relative}
  .flyer{position:absolute;left:50px;top:339px;width:1100px;height:1540px;background:var(--paper);overflow:hidden;box-shadow:0 18px 40px rgba(0,0,0,.25)}
  .flyer > *{position:absolute}
  .hero-art{left:0;top:0;width:1100px;height:800px}
  .brand{left:78px;top:35px;width:320px;text-align:center}
  .brand-disc{width:156px;height:156px;border-radius:50%;background:var(--green);margin:0 auto 14px}
  .brand-name{font-weight:700;color:var(--forest);font-size:22px;line-height:26px;white-space:nowrap}
  .years{left:105px;top:304px;height:56px;padding:0 14px;background:var(--green);border-radius:4px;color:#fff;font-weight:800;font-size:44px;line-height:58px;letter-spacing:-.5px}
  .headline{left:103px;top:372px;line-height:1;text-transform:uppercase}
  .headline .lead{display:block;font-weight:400;font-size:42px;color:var(--ink);letter-spacing:.3px;margin-bottom:4px}
  .headline .key{display:block;font-weight:800;font-size:56px;color:var(--forest);margin-bottom:2px}
  .headline .tail{display:block;font-weight:800;font-size:56px;color:var(--ink)}
  .intro{left:80px;top:630px;font-weight:400;font-size:17px;line-height:21px;color:var(--muted)}
  .intro p:first-child{width:560px;margin-bottom:10px}
  .intro p:last-child{width:760px}
  .gallery{left:0;top:833px;width:1100px;height:220px}
  .work-photo{position:absolute;top:0;width:218px;height:218px;border-radius:50%;border:6px solid var(--lime);box-shadow:0 4px 10px rgba(0,0,0,.25)}
  .work-photo.fence{left:72px;background:linear-gradient(160deg,#cfd6d8 0%,#9a6a45 35%,#7a4e31 70%,#5a5a5a 100%)}
  .work-photo.hedge{left:322px;background:radial-gradient(circle at 60% 45%,#4f7a32 0%,#2f5020 60%,#1e3314 100%)}
  .work-photo.planter{left:572px;background:linear-gradient(180deg,#5f8a3a 0%,#3f5a28 15%,#d8d8d8 16%,#c4c4c4 55%,#6a6a6a 56%,#4a4a4a 100%)}
  .work-photo.paving{left:824px;background:linear-gradient(150deg,#8a8a85 0%,#6f6f6b 50%,#5c5c58 100%)}
  .band{left:0;top:1100px;width:1100px;height:327px;background:var(--band)}
  .tab{left:359px;top:1070px;width:379px;height:68px;background:var(--lime);border:3px solid #fff;border-radius:4px;text-align:center;font-family:"Montserrat Alternates","Montserrat",sans-serif;font-weight:700;font-size:52px;line-height:60px;color:#2f3a20;box-shadow:0 3px 6px rgba(0,0,0,.3)}
  .band-intro{left:63px;top:1156px;width:960px;font-size:18px;line-height:22px;color:#f2f2f2}
  .service-list{list-style:none;top:1255px;font-weight:700;font-size:18px;line-height:29px;color:#fff;text-transform:uppercase}
  .service-list li{position:relative;padding-left:38px}
  .service-list li::before{content:"";position:absolute;left:0;top:7px;width:14px;height:14px;border:1.5px solid var(--lime);border-radius:50%}
  .service-list li::after{content:"";position:absolute;left:5px;top:10px;width:4px;height:6px;border:solid var(--lime);border-width:0 1.5px 1.5px 0;transform:rotate(45deg)}
  .col-a{left:65px}
  .col-b{left:416px;top:1266px}
  .col-c{left:720px;top:1266px}
  .divider{top:1250px;height:130px;border-left:2px dotted #8a8a8a}
  .divider.one{left:341px}
  .divider.two{left:660px}
  .contact{left:0;top:1427px;width:1100px;height:113px;font-family:"Montserrat Alternates","Montserrat",sans-serif;font-weight:700;color:var(--ink)}
  .contact-item{position:absolute;top:0;height:113px;display:flex;align-items:center;gap:14px;white-space:nowrap}
  .contact-item svg{flex:none}
  .contact-item.phone{left:64px;font-size:36px}
  .contact-item.mail{left:392px;font-size:23px}
  .contact-item.web{left:776px;font-size:23px}
  .contact-rule{position:absolute;top:24px;width:2px;height:60px;background:#9a9a9a}
  .contact-rule.one{left:360px}
  .contact-rule.two{left:740px}
</style>
</head>
<body>
<main class="flyer">
  <svg class="hero-art" viewBox="0 0 1100 800" width="1100" height="800">
    <defs>
      <linearGradient id="lawn" x1="0" y1="0" x2="1" y2="1">
        <stop offset="0" stop-color="#c9c2b6"/>
        <stop offset=".22" stop-color="#7fae3e"/>
        <stop offset=".6" stop-color="#4f8a2a"/>
        <stop offset=".85" stop-color="#b9b9b4"/>
        <stop offset="1" stop-color="#8c8a84"/>
      </linearGradient>
    </defs>
    <path class="swoosh-dark" fill="#0f8a3c" d="M0,520 C120,575 380,575 640,488 L640,502 C380,592 120,590 0,534 Z"/>
    <path class="swoosh-lime" fill="#abd037" d="M60,556 C230,622 470,590 660,508 L660,540 C460,628 220,632 60,556 Z"/>
    <circle cx="1040" cy="320" r="455" fill="#abd037"/>
    <circle cx="1047" cy="334" r="447" fill="#0f8a3c"/>
    <circle cx="1049" cy="320" r="436" fill="url(#lawn)" role="img" aria-label="Photo of a freshly mown green lawn with a pop-up sprinkler beside a stone-edged gravel border"/>
  </svg>

  <div class="brand">
    <div class="brand-disc"></div>
    <div class="brand-name">Greenvale Landscaping<br>Co Ltd</div>
  </div>

  <div class="years">25 YEARS</div>
  <h1 class="headline">
    <span class="lead">Experience in the</span>
    <span class="key">Landscaping</span>
    <span class="tail">Industry</span>
  </h1>

  <div class="intro">
    <p>With more than 25 years experience in the landscaping industry, Greenvale Landscaping Co offers services to large or small residential and commercial projects. Based in Canterbury, we are locally owned and operated.</p>
    <p>Whether you have a blank canvas or are looking to rejuvenate your property we are able to advise and make the process easy and stress free. From paving, pergolas and decks to concrete or planting your dream garden we have the expertise to help.</p>
  </div>

  <div class="gallery">
    <div class="work-photo fence" role="img" aria-label="Photo of a horizontal timber slat fence"></div>
    <div class="work-photo hedge" role="img" aria-label="Photo of a dense green hedge"></div>
    <div class="work-photo planter" role="img" aria-label="Photo of a concrete planter box on tiled paving"></div>
    <div class="work-photo paving" role="img" aria-label="Photo of exposed aggregate concrete paving"></div>
  </div>

  <div class="band"></div>
  <h2 class="tab">Services</h2>
  <p class="band-intro">As a full construction landscaping company, we formally offer the following services. However, we regularly work with clients who want something a little out of the box. If there is something in particular you are after, we are happy to discuss options with you.</p>

  <ul class="service-list col-a">
    <li>Patios</li><li>Paving</li><li>Concrete</li><li>Water Features</li><li>Decking</li>
  </ul>
  <div class="divider one"></div>
  <ul class="service-list col-b">
    <li>Fencing</li><li>Boardwalks</li><li>Timber</li><li>Planter Boxes</li><li>Pergolas</li>
  </ul>
  <div class="divider two"></div>
  <ul class="service-list col-c">
    <li>Retaining Walls</li><li>Gardens &amp; Lawns</li><li>Irrigation</li><li>Project Management</li><li>Consultation</li>
  </ul>

  <footer class="contact">
    <div class="contact-item phone">
      <svg width="34" height="34" viewBox="0 0 24 24" aria-hidden="true"><path fill="#abd037" d="M6.6 10.8a15.1 15.1 0 0 0 6.6 6.6l2.2-2.2c.3-.3.7-.4 1-.2 1.1.4 2.3.6 3.6.6.6 0 1 .4 1 1V20c0 .6-.4 1-1 1A17 17 0 0 1 3 4c0-.6.4-1 1-1h3.5c.6 0 1 .4 1 1 0 1.3.2 2.5.6 3.6.1.3 0 .7-.2 1z"/></svg>
      <span>021554872</span>
    </div>
    <div class="contact-rule one"></div>
    <div class="contact-item mail">
      <svg width="26" height="26" viewBox="0 0 24 24" aria-hidden="true"><rect x="2" y="5" width="20" height="14" rx="2" fill="none" stroke="#abd037" stroke-width="2.4"/><path d="M3 6l9 7 9-7" fill="none" stroke="#abd037" stroke-width="2.4"/></svg>
      <span>mark@brvkw.co.nz</span>
    </div>
    <div class="contact-rule two"></div>
    <div class="contact-item web">
      <svg width="28" height="28" viewBox="0 0 24 24" aria-hidden="true"><g fill="none" stroke="#abd037" stroke-width="2"><circle cx="12" cy="12" r="10"/><ellipse cx="12" cy="12" rx="4.5" ry="10"/><path d="M2 12h20M4 6.5h16M4 17.5h16"/></g></svg>
      <span>www.brvkw.co.nz</span>
    </div>
  </footer>
</main>
</body>
</html>
```